Business card for Mortgage broker business

I have already had the logo designed and am needing a great looking business card. My business focus is on servicing clients who may not be able to obtain finance through traditional lenders due to bad credit, short term employment or they just don't fit the banks profile. It needs to be professional, trust worthy but also have a caring fell about it.
I have provided files showing the green and black logo, the white logo(on white background so the file looks blank) and also a file with the white logo with a background of leaves that was made up which will probably be used for a website header.

Industry/Entity Type

Finance

Contact Information for Business Card

Marcus Dalby
Managing Director, Accredited Finance Broker(AFB)
Po Box 817, Harwood Vale VIC 3920
marcus@kestrelfunding.com.au
www.kestrelfunding.com.au
0438 216 507

Requirements
Nice to have
• I have added a picture of myself as I would like to see some designs with the pic in it, but I'm not sure if I want it on there with the logo's or just the logo's

```html
<!DOCTYPE html>
<html lang="en">
<head>
<meta charset="utf-8">
<title>Kestrel Funding – Business Card</title>
<link rel="stylesheet" href="https://fonts.googleapis.com/css2?family=Didact+Gothic&display=swap">
<style>
  :root {
    --page-bg: #b3b3b3;
    --card-light-top: #ffffff;
    --card-light-bottom: #e6e6e6;
    --card-dark: #14201d;
    --card-dark-edge: #0f1816;
    --brand-green: #137a3c;
    --text-light: #e9ecea;
    --text-muted: #c9cfcc;
  }
  html, body {
    margin: 0;
    padding: 0;
    width: 1200px;
    height: 1050px;
    overflow: hidden;
    background: var(--page-bg);
    font-family: "Didact Gothic", "Century Gothic", sans-serif;
  }
  .card {
    position: absolute;
    left: 264px;
    width: 672px;
    height: 384px;
    border-radius: 28px;
    overflow: hidden;
  }
  .card--front {
    top: 110px;
    background: linear-gradient(180deg, var(--card-light-top), var(--card-light-bottom));
  }
  .card--back {
    top: 574px;
    background: radial-gradient(ellipse at 50% 55%, #1b2925 0%, var(--card-dark) 60%, var(--card-dark-edge) 100%);
  }
  .card__art {
    position: absolute;
    inset: 0;
  }
  .brand {
    position: absolute;
    display: flex;
    align-items: center;
    gap: 10px;
    white-space: nowrap;
    line-height: 1;
  }
  .brand__dot {
    width: 13px;
    height: 13px;
    border-radius: 50%;
    background: currentColor;
  }
  .brand--front {
    left: 46px;
    top: 74px;
    font-size: 31px;
    color: var(--brand-green);
  }
  .brand--back {
    left: 50%;
    top: 194px;
    transform: translate(-50%, -50%);
    font-size: 35px;
    color: #ffffff;
  }
  .person {
    position: absolute;
    left: 35px;
    top: 226px;
    color: var(--text-light);
  }
  .person__name {
    margin: 0;
    font-size: 22px;
    font-weight: 400;
    line-height: 26px;
  }
  .person__role {
    margin: 0;
    font-size: 17px;
    line-height: 19px;
    color: var(--text-muted);
  }
  .contact {
    position: absolute;
    left: 35px;
    top: 306px;
    margin: 0;
    padding: 0;
    list-style: none;
    color: var(--text-muted);
    font-size: 17px;
  }
  .contact__item {
    display: flex;
    align-items: center;
    gap: 11px;
    height: 19.5px;
  }
  .contact__icon {
    width: 15px;
    height: 15px;
    fill: none;
    stroke: var(--text-muted);
    stroke-width: 1.4;
  }
  .address {
    position: absolute;
    left: 316px;
    top: 345px;
    margin: 0;
    font-size: 17px;
    line-height: 19px;
    color: var(--text-muted);
  }
</style>
</head>
<body>

<section class="card card--front" aria-label="Business card front">
  <svg class="card__art" width="672" height="384" viewBox="0 0 672 384">
    <defs>
      <linearGradient id="portraitTone" x1="0" y1="0" x2="0" y2="1">
        <stop offset="0" stop-color="#3a2a22"/>
        <stop offset="0.35" stop-color="#c98d6c"/>
        <stop offset="0.75" stop-color="#b47a5c"/>
        <stop offset="1" stop-color="#23252d"/>
      </linearGradient>
    </defs>
    <rect class="portrait" x="456" y="26" width="196" height="256" fill="url(#portraitTone)" role="img" aria-label="Portrait photo of the managing director"/>
    <path class="wave-green" fill="var(--brand-green)"
      d="M0,212 C60,166 160,156 300,196 C440,236 560,292 672,262 L672,306 C560,318 440,262 300,222 C170,184 60,186 0,230 Z"/>
    <path class="wave-dark" fill="var(--card-dark)"
      d="M0,222 C60,178 170,170 300,214 C440,262 560,318 672,304 L672,384 L0,384 Z"/>
  </svg>

  <div class="brand brand--front"><span class="brand__name">Kestrel Funding</span><span class="brand__dot"></span></div>

  <div class="person">
    <h1 class="person__name">Marcus Dalby</h1>
    <p class="person__role">Managing Director,<br>Accredited Finance Broker(AFB)</p>
  </div>

  <ul class="contact">
    <li class="contact__item">
      <svg class="contact__icon" viewBox="0 0 16 16"><path d="M3 1.5 L6 1.5 L7 5 L5 6.5 C6 9 7 10 9.5 11 L11 9 L14.5 10 L14.5 13 C14.5 14 13.5 14.5 12.5 14.5 C6.5 14 2 9.5 1.5 3.5 C1.5 2.5 2 1.5 3 1.5 Z" fill="var(--text-muted)" stroke="none"/></svg>
      <span>0438 216 507</span>
    </li>
    <li class="contact__item">
      <svg class="contact__icon" viewBox="0 0 16 16"><rect x="1" y="3" width="14" height="10" fill="var(--text-muted)" stroke="none"/><path d="M1 3 L8 9 L15 3" stroke="var(--card-dark)"/></svg>
      <span>marcus@kestrelfunding.com.au</span>
    </li>
    <li class="contact__item">
      <svg class="contact__icon" viewBox="0 0 16 16"><circle cx="8" cy="8" r="6.5"/><ellipse cx="8" cy="8" rx="3" ry="6.5"/><path d="M1.5 8 H14.5 M2.5 4.5 H13.5 M2.5 11.5 H13.5"/></svg>
      <span>www.kestrelfunding.com.au</span>
    </li>
  </ul>

  <p class="address">Po Box 817, Harwood Vale VIC 3920</p>
</section>

<section class="card card--back" aria-label="Business card back">
  <div class="brand brand--back"><span class="brand__name">Kestrel Funding</span><span class="brand__dot"></span></div>
</section>

</body>
</html>
```